Business Stationery - New Business card design

We are looking for some new business stationery, including business cards (double sided), compliment slips & letterheads for our offices in the UK, Ireland, North Carolina (US) & our Holdings company.

We are open to all ideas; however we are ideally looking for something that does not look corporate.

Our website is www.tallowmerefolk.com – this is the style of branding that we are currently using.

Here is some of the information that should be included;

Business Cards

Front
Logo
Name – Dominic Furnival
Job Title - Director
Direct line number - +353 (0)1 684 2710
Office number - +353 (0)1 692 4150
Email address – d.furnival@tallowmf.com
Website address – www.tallowmerefolk.com

Back
Logo
‘Specialists in IT Recruitment’
LinkedIn – Tallowmere Folk Partners
Twitter - @tallowhires
An image included – possibly ‘Image 1’ attached?

Letterheads & Compliment slips

UK (A4 size)
Logo
Phone numbers for the various offices;
London: +44 (0)20 7158 6240
Belfast: +44 (0)28 9186 3370
Dublin: +353 (0)1 692 4150
Raleigh, NC: +1 919 462 7300
Address: 2nd Floor, 84 Malvern Row, London W1C 7QZ
Email: info@tallowmf.com
Website: www.tallowmerefolk.com
Social media icons for LinkedIn & Twitter
Tallowmere Folk Partners Registered in England & Wales No. 8315726 VAT No. 871402396

Ireland (A4 size)
Logo
Address: 3-5 Lantern Street, Dublin 2 D02 KW81, Ireland
Email: info@tallowmf.com
Tallowmere Folk Partners (Ireland) Registered in Ireland No. 642093 VAT No. 5817320KK

USA (letter size)

Logo
Address: 845 N. Pemberly Street, Raleigh, North Carolina 27605, United States
Email: info@tallowmf.com
Tallowmere Folk Partners Inc. Registered in the State of North Carolina No. 2936410

Holdings (A4 size)

Logo
Address: 17 Quillon Street, Belfast BT27JD
Email: info@tallowmf.com
Tallowmere Folk Partners (Holdings) Ltd Registered in Northern Ireland No. NI735208

Target Market(s)

IT Professionals

Industry/Entity Type

It Professional

Contact Information for Business Card

Front
Logo
Name – Dominic Furnival
Job Title - Director

Back
Logo
Twitter - @tallowhires

```html
<!DOCTYPE html>
<html lang="en">
<head>
<meta charset="utf-8">
<title>Tallowmere Folk Partners – Business Card</title>
<link href="https://fonts.googleapis.com/css2?family=Montserrat:wght@500;600;700&family=Roboto:wght@400&display=swap" rel="stylesheet">
<style>
  :root {
    --bg: #2b2b2d;
    --blue: #1a63b5;
    --blue-light: #2a86c9;
    --blue-deep: #1553a8;
    --green: #6cbb53;
    --white: #ffffff;
    --ink-blue: #1d5fae;
  }
  html, body {
    margin: 0;
    width: 1200px;
    height: 929px;
    overflow: hidden;
    background: var(--bg);
  }
  .canvas {
    position: relative;
    width: 1200px;
    height: 929px;
  }
  .card {
    position: absolute;
    width: 620px;
    height: 354px;
    border-radius: 16px;
    overflow: hidden;
    box-shadow: 0 10px 30px rgba(0,0,0,.5);
  }

  /* Back of card */
  .card--back { left: 50px; top: 70px; background: var(--blue); }
  .card--back .illustration {
    position: absolute;
    left: 60px; top: 40px;
    width: 330px; height: 200px;
    border-radius: 10px;
    background: linear-gradient(135deg, #e8f1f4 0%, #f2c75e 45%, #e2634e 100%);
    opacity: .9;
  }
  .card--back .tagline {
    position: absolute;
    left: 60px; bottom: 56px;
    width: 330px;
    margin: 0;
    text-align: center;
    font: 500 17px/1 "Montserrat", sans-serif;
    letter-spacing: 1.5px;
    color: var(--white);
  }
  .card--back .brand-panel {
    position: absolute;
    right: 0; top: 0;
    width: 180px; height: 100%;
    background: var(--green);
  }

  /* Wordmark set vertically, two lines, one colour and weight */
  .wordmark {
    position: absolute;
    top: 50%; left: 50%;
    transform: translate(-50%, -50%) rotate(-90deg);
    display: flex;
    flex-direction: column;
    align-items: center;
    white-space: nowrap;
    font: 600 28px/1.15 "Montserrat", sans-serif;
    letter-spacing: 1px;
  }
  .brand-panel .wordmark { color: var(--white); }

  /* Front of card */
  .card--front { left: 530px; top: 505px; background: linear-gradient(160deg, var(--blue-light) 0%, var(--blue-deep) 70%); }
  .card--front .brand-panel {
    position: absolute;
    left: 0; top: 0;
    width: 200px; height: 100%;
    background: var(--white);
  }
  .card--front .brand-panel .wordmark { color: var(--ink-blue); }
  .details {
    position: absolute;
    left: 232px; top: 48px;
    right: 20px;
  }
  .person-name {
    margin: 0;
    font: 700 27px/1.1 "Montserrat", sans-serif;
    color: var(--white);
  }
  .person-title {
    margin: 4px 0 0;
    font: 600 19px/1.1 "Montserrat", sans-serif;
    color: var(--green);
  }
  .contact-list {
    list-style: none;
    margin: 44px 0 0;
    padding: 0;
    font: 400 15px/1 "Roboto", sans-serif;
    color: var(--white);
  }
  .contact-list li {
    display: flex;
    align-items: center;
    gap: 9px;
    height: 24px;
  }
  .contact-list svg { width: 15px; height: 15px; flex: none; }
</style>
</head>
<body>
<main class="canvas">

  <section class="card card--back" aria-label="Card back">
    <div class="illustration" role="img" aria-label="Isometric illustration of office towers, a coffee cup and stacked devices under clouds and planes"></div>
    <p class="tagline">Specialists in IT Recruitment</p>
    <div class="brand-panel">
      <span class="wordmark"><span>Tallowmere</span><span>Folk Partners</span></span>
    </div>
  </section>

  <section class="card card--front" aria-label="Card front">
    <div class="brand-panel">
      <span class="wordmark"><span>Tallowmere</span><span>Folk Partners</span></span>
    </div>
    <div class="details">
      <h1 class="person-name">Dominic Furnival</h1>
      <p class="person-title">Managing Director</p>
      <ul class="contact-list">
        <li>
          <svg viewBox="0 0 16 16" aria-hidden="true"><path fill="#6cbb53" d="M3 1l3 3-1.5 2a9 9 0 0 0 5.5 5.5L12 10l3 3-2 2C6 15 1 10 1 3z"/></svg>
          +353 (0)1 684 2710
        </li>
        <li>
          <svg viewBox="0 0 16 16" aria-hidden="true"><path fill="#6cbb53" d="M1 5q7-5 14 0v2h-3V5H4v2H1zM3 8h10l1 6H2z"/></svg>
          +353 (0)1 692 4150
        </li>
        <li>
          <svg viewBox="0 0 16 16" aria-hidden="true"><rect x="1" y="3" width="14" height="10" fill="#6cbb53"/><path d="M1 3l7 6 7-6" stroke="#1a63b5" stroke-width="1.3" fill="none"/></svg>
          d.furnival@tallowmf.com
        </li>
        <li>
          <svg viewBox="0 0 16 16" aria-hidden="true"><circle cx="8" cy="8" r="7" fill="#6cbb53"/><path d="M1 8h14M8 1c-3 4-3 10 0 14M8 1c3 4 3 10 0 14" stroke="#1a63b5" stroke-width="1" fill="none"/></svg>
          www.tallowmerefolk.com
        </li>
        <li>
          <svg viewBox="0 0 16 16" aria-hidden="true"><rect x="1" y="1" width="14" height="14" rx="2" fill="#6cbb53"/></svg>
          @tallowhires
        </li>
        <li>
          <svg viewBox="0 0 16 16" aria-hidden="true"><rect x="1" y="1" width="14" height="14" rx="2" fill="#6cbb53"/></svg>
          Tallowmere Folk Partners
        </li>
      </ul>
    </div>
  </section>

</main>
</body>
</html>
```